Innovative Bitcoin Powerpoint Presentation

I have constructred most of the data for a 15 page powerpoint presentation on an innovative bitcoin idea that provides access to fiat currency with bitcoin hodlings

I need this to look great as a first blush to potential investors

Reason: updated deck and name

Target Market(s)

Venture Capital firms and private equity firms

Requirements
Must have
• Fun, innovateive deck, very clean
Should not have
• any generic feel - no templates

```html
<!DOCTYPE html>
<html lang="en">
<head>
<meta charset="utf-8">
<title>Velocoin Investor Deck</title>
<link href="https://fonts.googleapis.com/css2?family=Montserrat:wght@400;500;600;700&display=swap" rel="stylesheet">
<style>
  :root {
    --backdrop: #161616;
    --slide-light: #f1f2f2;
    --ink: #111111;
    --text: #434343;
    --orange: #f5a44a;
    --teal: #2fb39a;
    --blue: #2f74b8;
    --grey-line: #777777;
    --brand: #6b1236;
  }
  * { margin: 0; padding: 0; box-sizing: border-box; }
  html, body { width: 1200px; height: 1200px; overflow: hidden; }
  body {
    background: radial-gradient(ellipse at center, #262626 0%, var(--backdrop) 70%);
    font-family: "Montserrat", sans-serif;
    position: relative;
  }
  .slide {
    position: absolute;
    left: 202px;
    width: 812px;
    height: 507px;
    overflow: hidden;
  }
  .slide--opportunity { top: 52px; }
  .slide--solution { top: 607px; }
  .slide__backdrop {
    position: absolute; inset: 0;
    background: linear-gradient(135deg, #cfcfcf 0%, #e4e4e4 25%, var(--slide-light) 50%, #e2e2e2 75%, #d9d9d9 100%);
  }
  .slide__rule {
    position: absolute; left: 0; top: 50px; width: 604px; height: 2px;
    background: linear-gradient(90deg, var(--blue) 0%, var(--grey-line) 18%, var(--orange) 45%, var(--orange) 60%, var(--teal) 100%);
  }
  .brand {
    position: absolute; left: 624px; top: 30px;
    display: flex; align-items: flex-start; gap: 6px;
  }
  .brand__dot {
    width: 30px; height: 30px; border-radius: 50%;
    background: var(--brand); margin-top: 2px;
  }
  .brand__text { display: flex; flex-direction: column; align-items: flex-end; }
  .brand__name { font-size: 25px; font-weight: 600; color: var(--ink); line-height: 1; letter-spacing: -0.3px; }
  .brand__tagline { font-size: 8px; font-weight: 500; color: var(--text); letter-spacing: 0.8px; margin-top: 3px; }
  .slide__title {
    position: absolute; left: 38px; top: 140px;
    font-size: 32px; font-weight: 700; color: var(--ink); line-height: 1; letter-spacing: -0.6px;
    white-space: nowrap;
  }
  .slide--opportunity .slide__title .initial { color: var(--orange); }
  .slide--solution .slide__title .initial { color: var(--teal); }
  .point, .subpoint, .detail, .marker {
    position: absolute; line-height: 1; white-space: nowrap;
  }
  .point { left: 299px; font-size: 16.5px; font-weight: 600; color: var(--text); }
  .subpoint { left: 328px; font-size: 13.3px; font-weight: 400; color: var(--text); }
  .detail { left: 357px; font-size: 13.3px; font-weight: 400; color: var(--text); }
  .marker { font-weight: 700; }
  .marker--plus { left: 274px; font-size: 19px; }
  .marker--dash { left: 307px; font-size: 14px; }
  .slide--opportunity .marker { color: var(--orange); }
  .slide--solution .marker { color: var(--teal); }
  .page-tab { position: absolute; left: 727px; top: 427px; width: 85px; height: 64px; }
  .page-tab__label {
    position: absolute; right: 19px; top: 441px;
    color: #ffffff; font-size: 14px; line-height: 1.3; text-align: right;
  }
  .page-tab__label b { display: block; font-weight: 700; }
</style>
</head>
<body>

<section class="slide slide--opportunity">
  <div class="slide__backdrop" role="img" aria-label="Soft grey faceted low-poly background"></div>
  <div class="slide__rule"></div>
  <div class="brand">
    <span class="brand__dot"></span>
    <div class="brand__text">
      <span class="brand__name">Velocoin</span>
      <span class="brand__tagline">Coins that travel</span>
    </div>
  </div>
  <h2 class="slide__title"><span class="initial">O</span>pportunity</h2>

  <span class="marker marker--plus" style="top:150px">+</span>
  <span class="point" style="top:151px">Highly inefficient BTC/Fiat exchange process</span>
  <span class="marker marker--dash" style="top:175px">-</span>
  <span class="subpoint" style="top:177px">Wide bid/ask spreads</span>
  <span class="marker marker--dash" style="top:194px">-</span>
  <span class="subpoint" style="top:196px">High transaction Fees</span>
  <span class="marker marker--dash" style="top:213px">-</span>
  <span class="subpoint" style="top:215px">Volatile price movement</span>

  <span class="marker marker--plus" style="top:257px">+</span>
  <span class="point" style="top:258px">Increasing BTC adoption rates</span>
  <span class="marker marker--dash" style="top:282px">-</span>
  <span class="subpoint" style="top:284px">Technical trends point to mass adoption of BTC</span>

  <span class="marker marker--plus" style="top:325px">+</span>
  <span class="point" style="top:326px">Leveraging BTC remains a challenge</span>
  <span class="marker marker--dash" style="top:350px">-</span>
  <span class="subpoint" style="top:352px">Inverse relationship between fiat/BTC ownership</span>

  <svg class="page-tab" viewBox="0 0 85 64" aria-hidden="true">
    <polygon points="0,0 85,9 85,49 27,63" fill="var(--blue)"/>
  </svg>
  <div class="page-tab__label">Page<b>3</b></div>
</section>

<section class="slide slide--solution">
  <div class="slide__backdrop" role="img" aria-label="Soft grey faceted low-poly background"></div>
  <div class="slide__rule"></div>
  <div class="brand">
    <span class="brand__dot"></span>
    <div class="brand__text">
      <span class="brand__name">Velocoin</span>
      <span class="brand__tagline">Coins that travel</span>
    </div>
  </div>
  <h2 class="slide__title"><span class="initial">S</span>olution</h2>

  <span class="marker marker--plus" style="top:150px">+</span>
  <span class="point" style="top:151px">Line of credit secured by a users Bitcoin wallet value</span>

  <span class="marker marker--plus" style="top:196px">+</span>
  <span class="point" style="top:197px">Instant access to local fiat currency</span>
  <span class="marker marker--dash" style="top:221px">-</span>
  <span class="subpoint" style="top:223px">Debit cards provides global access</span>
  <span class="detail" style="top:246px">ATM Withdrawals</span>
  <span class="detail" style="top:268px">Point of Sale Purchase</span>
  <span class="marker marker--dash" style="top:282px">-</span>

  <span class="marker marker--plus" style="top:310px">+</span>
  <span class="point" style="top:311px">Lower transaction costs</span>
  <span class="marker marker--dash" style="top:335px">-</span>
  <span class="subpoint" style="top:337px">No bid/ask spreads</span>

  <span class="marker marker--plus" style="top:379px">+</span>
  <span class="point" style="top:380px">Increased purchasing power</span>

  <span class="marker marker--plus" style="top:424px">+</span>
  <span class="point" style="top:425px">Fundline</span>

  <svg class="page-tab" viewBox="0 0 85 64" aria-hidden="true">
    <polygon points="0,0 85,9 85,49 27,63" fill="var(--blue)"/>
  </svg>
  <div class="page-tab__label">Page<b>4</b></div>
</section>

</body>
</html>
```